Figure for Manufacture of Wound Healing Gel

Who we are: We are a nationally funded bioengineering laboratory at Harlow Ridge University conducting research on the tendon healing properties of a gel manufactured from real tendon.

What we need: We require a figure piece that will be included in an academic publication. With that in mind, the figure must be professional, clear, and concise. A reader would need to glance at the figure for only a moment to understand the process of how we manufacture and store tendon gel. Actual pictures of the in-between steps are included and will need to be cropped to improve the professional look of the design.

The Details: The figure should stepwise show the process of how we manufacture and store tendon gel. In brief, we harvest tendon from donor cadavers. Those tendons undergo decellularization, lyophilization (fancy word for freeze-drying), and are milled into a fine powder. The powder is set in acidified water and treated with digestive enzymes. After 24 hrs, the gel is brought to physiologic pH and salinity and placed in vials. The vials are frozen and again lyophilized (this is so they can be stored and transported easily). Finally the samples are reconstituted with DI water.

The Figure: Should be a linear process (horizontal). The following are the actual steps we wish to include (steps need not be numbered necessarily as long as they are in logical order...

1.) A picture of harvested tendon (Step 1.jpg)
2.) Written description: "Decellularization, lyophilization, and milling"
3.) A picture of milled tendon powder (Step 2.jpg)
4.) Written description: "Digestion with pepsin before establishing physiologic pH and salinity".
5.) A picture of gel (Step 3.jpg)
6.) Written description: "Lyophilization of aliquots"
7.) A picture of freeze-dried gel (Step 4.jpg)
8.) Written description: "Reconstitution with DI water"
9.) A picture of reconstituted gel (Step 5.jpg)

Feel free to message for any questions, comments, or clarifications.

```html
<!DOCTYPE html>
<html lang="en">
<head>
<meta charset="utf-8">
<title>How We Manufacture and Store Tendon Gel</title>
<link rel="stylesheet" href="https://fonts.googleapis.com/css2?family=Cormorant+Garamond:wght@500&family=Open+Sans:ital,wght@1,400&display=swap">
<style>
  :root {
    --band-red: #c10000;
    --title-white: #ffffff;
    --bg-center: #ffffff;
    --bg-edge: #d6d6d6;
    --frame-white: #ffffff;
    --arrow-dark: #151515;
    --arrow-light: #5a5a5a;
    --arrow-text: #ffffff;
  }
  html, body {
    margin: 0;
    padding: 0;
    width: 1200px;
    height: 478px;
    overflow: hidden;
  }
  .figure {
    position: relative;
    width: 1200px;
    height: 478px;
    overflow: hidden;
    background: radial-gradient(ellipse 700px 320px at 560px 200px, var(--bg-center) 0%, #ececec 55%, var(--bg-edge) 100%);
  }
  .title-band {
    position: absolute;
    left: 0; top: 0;
    width: 1200px;
    height: 145px;
    background: var(--band-red);
  }
  .title {
    position: absolute;
    left: 0; right: 0;
    top: 74px;
    margin: 0;
    text-align: center;
    font-family: "Cormorant Garamond", "Times New Roman", serif;
    font-weight: 500;
    font-size: 45px;
    letter-spacing: 3.2px;
    line-height: 50px;
    color: var(--title-white);
  }
  .step-photo {
    position: absolute;
    box-sizing: border-box;
    border: 3px solid var(--frame-white);
    box-shadow: 1px 2px 4px rgba(0,0,0,0.35);
  }
  .step-photo--tendon   { left: 20px;   top: 236px; width: 129px; height: 96px;
    background: radial-gradient(ellipse at 45% 45%, #b9ad93 0%, #6f6a60 40%, #2e2e2e 100%); }
  .step-photo--powder   { left: 290px;  top: 236px; width: 129px; height: 96px;
    background: radial-gradient(ellipse at 50% 45%, #e6dcc2 0%, #8e8a82 45%, #353535 100%); }
  .step-photo--gel      { left: 566px;  top: 236px; width: 131px; height: 96px;
    background: radial-gradient(ellipse at 50% 48%, #f2f2ee 0%, #bdbdba 18%, #5d5d5d 50%, #2b2b2b 100%); }
  .step-photo--dried    { left: 862px;  top: 233px; width: 73px;  height: 99px;
    background: linear-gradient(90deg, #3a3a3a 0%, #cfcfcf 30%, #e2e2e0 55%, #b4b4b4 75%, #3a3a3a 100%); }
  .step-photo--reconstituted { left: 1104px; top: 233px; width: 72px; height: 99px;
    background: linear-gradient(90deg, #2f2f2f 0%, #c8c8c4 30%, #e6e3da 55%, #b0b0ac 75%, #2f2f2f 100%); }

  .step-arrow {
    position: absolute;
    width: 128px;
    height: 74px;
  }
  .step-arrow svg {
    position: absolute;
    left: 0; top: 0;
    filter: drop-shadow(1px 2px 2px rgba(0,0,0,0.35));
  }
  .step-arrow__label {
    position: absolute;
    left: 24px;
    right: 18px;
    top: 50%;
    transform: translateY(-50%);
    font-family: "Open Sans", Arial, sans-serif;
    font-style: italic;
    font-size: 11px;
    line-height: 13px;
    color: var(--arrow-text);
  }
  .step-arrow--one   { left: 154px; top: 245px; }
  .step-arrow--two   { left: 425px; top: 245px; }
  .step-arrow--three { left: 717px; top: 247px; }
  .step-arrow--four  { left: 946px; top: 247px; }
  .step-arrow--two .step-arrow__label { left: 14px; }
</style>
</head>
<body>
<main class="figure">
  <header class="title-band">
    <h1 class="title">HOW WE MANUFACTURE AND STORE TENDON GEL</h1>
  </header>

  <div class="step-photo step-photo--tendon" role="img" aria-label="Photo of harvested tendons in a glass dish"></div>

  <div class="step-arrow step-arrow--one">
    <svg width="128" height="74" viewBox="0 0 128 74" aria-hidden="true">
      <defs>
        <linearGradient id="arrow-fill" x1="0" y1="1" x2="1" y2="0">
          <stop offset="0" stop-color="var(--arrow-dark)"/>
          <stop offset="0.6" stop-color="#2a2a2a"/>
          <stop offset="1" stop-color="var(--arrow-light)"/>
        </linearGradient>
      </defs>
      <polygon points="2,2 110,2 126,37 110,72 2,72 10,37" fill="url(#arrow-fill)" stroke="#ffffff" stroke-width="2"/>
    </svg>
    <p class="step-arrow__label" style="margin:0">Decellularization, lyophilization, and milling</p>
  </div>

  <div class="step-photo step-photo--powder" role="img" aria-label="Photo of milled tendon powder in a glass dish"></div>

  <div class="step-arrow step-arrow--two">
    <svg width="128" height="74" viewBox="0 0 128 74" aria-hidden="true">
      <polygon points="2,2 110,2 126,37 110,72 2,72 10,37" fill="url(#arrow-fill)" stroke="#ffffff" stroke-width="2"/>
    </svg>
    <p class="step-arrow__label" style="margin:0">Digestion with pepsin before establishing physiologic pH and salinity</p>
  </div>

  <div class="step-photo step-photo--gel" role="img" aria-label="Photo of tendon gel in a glass dish"></div>

  <div class="step-arrow step-arrow--three">
    <svg width="128" height="74" viewBox="0 0 128 74" aria-hidden="true">
      <polygon points="2,2 110,2 126,37 110,72 2,72 10,37" fill="url(#arrow-fill)" stroke="#ffffff" stroke-width="2"/>
    </svg>
    <p class="step-arrow__label" style="margin:0">Lyophilization of aliquots</p>
  </div>

  <div class="step-photo step-photo--dried" role="img" aria-label="Photo of a vial with freeze-dried gel"></div>

  <div class="step-arrow step-arrow--four">
    <svg width="128" height="74" viewBox="0 0 128 74" aria-hidden="true">
      <polygon points="2,2 110,2 126,37 110,72 2,72 10,37" fill="url(#arrow-fill)" stroke="#ffffff" stroke-width="2"/>
    </svg>
    <p class="step-arrow__label" style="margin:0">Reconstitution with DI water</p>
  </div>

  <div class="step-photo step-photo--reconstituted" role="img" aria-label="Photo of a vial with reconstituted gel"></div>
</main>
</body>
</html>
```